Business Card and Letterhead for Vantage Psychology

We need a business card design and letterhead to use for our Psychology firm that specializes in psychoeducational assessments and individual therapy. Our motto is Purpose-Driven Assessments, Meaning-Centered Therapy.Our contact information is as follows:
Vantage Psychology
The Marwick Block - 6127-48St.
Box 2716 Elmford, AB
T2K 3M8
t 403.555.0148 (VANT)
f 403.555.0172
www.vantagepsychology-example.ca
The business card will be used for two different psychologists so I can supply names nearer to completion. We prefer clean, uncluttered looks.

Target Market(s)

Clients, Educators

Font styles to use
Sans Serif

Colors

Designer to choose colors to be used in the design.

Requirements
Must have
• All relevant contact info, logo, some "white" space.
Nice to have
• It would be nice to see letterhead options that have the logo on the top of the page but also options that have it on the side. I think top of the page is probably our preference.
Should not have
• Too much clutter!

```html
<!DOCTYPE html>
<html lang="en">
<head>
<meta charset="utf-8">
<title>Vantage Psychology — Business Card and Letterhead</title>
<link href="https://fonts.googleapis.com/css2?family=Lato:wght@400;700&display=swap" rel="stylesheet">
<style>
  :root{
    --backdrop:#3a3a3a;
    --paper:#ffffff;
    --blue:#4fb8d8;
    --orange:#f39a4f;
    --ink:#1e1e1e;
  }
  *{box-sizing:border-box;margin:0;padding:0}
  html,body{width:1200px;height:514px;overflow:hidden}
  body{background:var(--backdrop);font-family:'Lato',sans-serif;position:relative}

  .sheet{position:absolute;background:var(--paper);border-top:4px solid var(--blue);border-bottom:4px solid var(--orange);box-shadow:0 4px 14px rgba(0,0,0,.35)}

  .brand{display:flex;flex-direction:column;align-items:center;gap:5px}
  .brand-dot{border-radius:50%;background:var(--blue)}
  .brand-name{color:var(--blue);font-weight:400;letter-spacing:.08em;text-transform:uppercase;white-space:nowrap}

  .icon{width:1em;height:1em;flex:none;fill:var(--orange)}
  .contact-list{list-style:none;color:var(--ink)}
  .contact-list li{display:flex;align-items:center;gap:.5em;white-space:nowrap}

  /* Business card back */
  .card-back{left:50px;top:30px;width:380px;height:217px;display:flex;align-items:center;justify-content:center;border-top-width:6px;border-bottom-width:6px}
  .card-back .brand-dot{width:58px;height:58px}
  .card-back .brand-name{font-size:22px}

  /* Business card front */
  .card-front{left:50px;top:267px;width:380px;height:217px;border-top-width:6px;border-bottom-width:6px;display:flex;align-items:center;padding:0 20px}
  .card-front .brand{width:140px}
  .card-front .brand-dot{width:40px;height:40px}
  .card-front .brand-name{font-size:12px}
  .card-divider{width:1.5px;height:120px;background:var(--blue);margin:0 16px}
  .card-person .person-name{font-size:17px;font-weight:700;color:var(--blue)}
  .card-person .person-role{font-size:13px;color:var(--orange);margin-bottom:8px}
  .card-person .contact-list{font-size:9px;line-height:1.55}

  /* Letterheads */
  .letterhead{top:27px;width:320px;height:453px}
  .letterhead-side{left:515px}
  .letterhead-centre{left:855px}
  .letterhead .brand-dot{width:30px;height:30px}
  .letterhead .brand-name{font-size:8.5px}
  .letterhead-side .brand{position:absolute;left:26px;top:18px}
  .letterhead-side .contact-list{position:absolute;left:222px;top:33px;font-size:4.6px;line-height:1.55}
  .letterhead-centre .brand{position:absolute;left:0;right:0;top:18px}
  .letterhead-footer{position:absolute;left:18px;right:18px;bottom:14px;display:flex;justify-content:space-between;font-size:4.3px}
</style>
</head>
<body>

<svg width="0" height="0" style="position:absolute" aria-hidden="true">
  <symbol id="i-pin" viewBox="0 0 10 10"><path d="M5 0a3.5 3.5 0 0 0-3.5 3.5C1.5 6 5 10 5 10s3.5-4 3.5-6.5A3.5 3.5 0 0 0 5 0zm0 5a1.4 1.4 0 1 1 0-2.8A1.4 1.4 0 0 1 5 5z"/></symbol>
  <symbol id="i-mail" viewBox="0 0 10 10"><path d="M0 2h10v6H0zM1 3v.4l4 2.4 4-2.4V3z"/></symbol>
  <symbol id="i-phone" viewBox="0 0 10 10"><path d="M2 .5l2 2-1 1.3c.6 1.3 1.7 2.4 3 3l1.3-1 2 2L8 9.5C4 9.5.5 6 .5 2z"/></symbol>
  <symbol id="i-fax" viewBox="0 0 10 10"><path d="M2.5 1h5v2.5h-5zM1 4h8v5H1zm1.5 1.5v1h5v-1z"/></symbol>
  <symbol id="i-web" viewBox="0 0 10 10"><path d="M5 0a5 5 0 1 0 0 10A5 5 0 0 0 5 0zm0 1c.6.7 1 1.9 1.1 3.4H3.9C4 2.9 4.4 1.7 5 1zM1.1 5.5h1.8c.1 1.2.4 2.2.8 3A4 4 0 0 1 1.1 5.5zm0-1.1a4 4 0 0 1 2.6-2.9c-.4.8-.7 1.8-.8 2.9zM5 9c-.6-.7-1-1.9-1.1-3.5h2.2C6 7.1 5.6 8.3 5 9zm1.3-.5c.4-.8.7-1.8.8-3h1.8a4 4 0 0 1-2.6 3zm.8-4.1c-.1-1.1-.4-2.1-.8-2.9a4 4 0 0 1 2.6 2.9z"/></symbol>
</svg>

<section class="sheet card-back" aria-label="Business card back">
  <div class="brand">
    <span class="brand-dot"></span>
    <span class="brand-name">Vantage Psychology</span>
  </div>
</section>

<section class="sheet card-front" aria-label="Business card front">
  <div class="brand">
    <span class="brand-dot"></span>
    <span class="brand-name">Vantage Psychology</span>
  </div>
  <div class="card-divider"></div>
  <div class="card-person">
    <p class="person-name">Your Name</p>
    <p class="person-role">psychologist</p>
    <ul class="contact-list">
      <li><svg class="icon"><use href="#i-pin"/></svg>The Marwick Block-6127-48St.</li>
      <li><svg class="icon"><use href="#i-mail"/></svg>2716 Elmford,AB T2K 3M8</li>
      <li><svg class="icon"><use href="#i-phone"/></svg>555-555-0148 (VANT)</li>
      <li><svg class="icon"><use href="#i-fax"/></svg>555-555-0172</li>
      <li><svg class="icon"><use href="#i-web"/></svg>www.vantagepsychology-example.ca</li>
    </ul>
  </div>
</section>

<section class="sheet letterhead letterhead-side" aria-label="Letterhead with contact block top right">
  <div class="brand">
    <span class="brand-dot"></span>
    <span class="brand-name">Vantage Psychology</span>
  </div>
  <ul class="contact-list">
    <li><svg class="icon"><use href="#i-pin"/></svg>The Marwick Block-6127-48St.</li>
    <li><svg class="icon"><use href="#i-mail"/></svg>2716 Elmford,AB T2K 3M8</li>
    <li><svg class="icon"><use href="#i-phone"/></svg>555-555-0148 (VANT)</li>
    <li><svg class="icon"><use href="#i-fax"/></svg>555-555-0172</li>
    <li><svg class="icon"><use href="#i-web"/></svg>www.vantagepsychology-example.ca</li>
  </ul>
</section>

<section class="sheet letterhead letterhead-centre" aria-label="Letterhead with centred header and contact footer">
  <div class="brand">
    <span class="brand-dot"></span>
    <span class="brand-name">Vantage Psychology</span>
  </div>
  <ul class="contact-list letterhead-footer">
    <li><svg class="icon"><use href="#i-pin"/></svg>The Marwick Block-6127-48St.</li>
    <li><svg class="icon"><use href="#i-mail"/></svg>2716 Elmford,AB T2K 3M8</li>
    <li><svg class="icon"><use href="#i-phone"/></svg>555-555-0148 (VANT)</li>
    <li><svg class="icon"><use href="#i-fax"/></svg>555-555-0172</li>
    <li><svg class="icon"><use href="#i-web"/></svg>www.vantagepsychology-example.ca</li>
  </ul>
</section>

</body>
</html>
```